Home page design layout for commercial driving school

- This is for a layout design of the home page only. No coding required.

- The design must be based around the attached HPID (home page information design). The table boxes are just for approximate placement of information – you DON'T have to make it look exactly like this. Information only is in orange text. Copy to go on the design in black text. Some instructions are in the HPID. Please be creative! You don’t have to use the exact images provided if you have a better idea.

- The design needs to be professional and modern. Fonts used except in the header must be Google fonts.

I've attached:
- HPID (information design) as a Word doc and PDF
- the logo. Please use the colours from the logos in the website design. Lots of white too.
- images for the gallery
- icon examples for the buttons for under the gallery - these aren't high resolution. If you have access to better examples please use those instead.
- logos of accreditations for that section
- background image that you may or may not use. This image is used in the business folders and business cards and I've got an example in this folder. If you can incorporate this into the design you may but it's not compulsory.

The winning PSD file will have to be provided as follows…
1. Canvas size of 2000px x 2000px - 72ppi in Adobe Photoshop (CS5 compatible)
2. Width of content section is 1100px wide - centered in the canvas
3. Header height (without nav bar) 150-160 pixels.
4. Any button rollovers/hovers in the PSD as hidden layers.
5. All fonts used must be Google fonts (except for the header fonts).
6. You will need to supply the chosen home page plus one example page (example page as a style guide for how all other pages will look). Example page is only the header and navigational bar at the top, an empty sector in the middle with a column (180 px wide) which can be left or right aligned which means the main sector is 920 pixels wide, and then the footer at the bottom of the page.

Apologies for the delay in assigning a first place for this project. We will be completing this project as soon as we can.

```html
<!DOCTYPE html>
<html lang="en">
<head>
<meta charset="utf-8">
<title>Keystone Drive Services – Driver Training</title>
<link href="https://fonts.googleapis.com/css2?family=Open+Sans:ital,wght@0,400;0,600;0,700;1,400;1,600&display=swap" rel="stylesheet">
<style>
:root{
  --navy:#2b2a6b;
  --navy-deep:#1f1d57;
  --ink:#1a1a1a;
  --text:#222;
  --white:#fff;
  --line:#333;
  --tick:#555;
  --sky:#a9c6e0;
  --grass:#8a7a52;
  --asphalt:#6d6d6d;
  --hazard:#f28a1a;
  --chip:#d9d9d9;
}
*{box-sizing:border-box;margin:0;padding:0}
html,body{width:1200px;height:900px;overflow:hidden;background:var(--white)}
body{position:relative;font-family:"Open Sans",Arial,sans-serif;color:var(--text)}
.abs{position:absolute}

/* Header */
.brand{left:147px;top:14px;width:130px;height:122px;display:flex;flex-direction:column;align-items:center;justify-content:center;gap:6px}
.brand-dot{width:60px;height:60px;border-radius:50%;background:var(--navy)}
.brand-name{font-size:12px;font-weight:700;color:var(--navy);text-align:center;line-height:1.2}
.header-info{left:289px;top:77px;font-size:10.3px;line-height:23.5px}
.header-pitch{right:165px;top:56px;text-align:right}
.header-pitch h1{font-size:14.5px;font-weight:700;color:var(--ink);margin-bottom:6px}
.header-pitch p{font-size:10.3px;line-height:12.5px}
.header-pitch .tagline{font-size:13.5px;font-style:italic;margin-top:10px}

/* Navigation */
.main-nav{left:132px;top:149px;width:897px;height:22px;background:var(--navy);border-bottom:2px solid var(--navy-deep)}
.main-nav a{position:absolute;top:4px;font-size:10.5px;font-weight:700;color:var(--white);text-decoration:none}

/* Gallery */
.gallery-main{left:132px;top:181px;width:522px;height:233px;background:linear-gradient(180deg,#5d7a55 0%,#7e8c72 45%,#9b9b96 70%,var(--asphalt) 100%)}
.gallery-side{left:684px;top:181px;width:345px;height:233px;background:linear-gradient(180deg,var(--sky) 0%,#c3d3df 35%,var(--grass) 48%,#a79b78 62%,#8a8a88 80%,var(--asphalt) 100%)}

/* Course buttons */
.course-icons{left:229px;top:427px;display:flex;gap:21.5px}
.course-icon{width:50px;height:50px;border:1.5px solid var(--line);background:var(--white);display:flex;align-items:center;justify-content:center}
.course-icon svg{width:42px;height:42px}
.course-icon .solid{fill:var(--ink)}
.course-icon .cut{fill:var(--white)}
.course-icon .stroke{fill:none;stroke:var(--ink);stroke-width:2.2;stroke-linecap:round}

/* Info columns */
.info-col{top:498px;font-size:10.3px;line-height:11.8px;white-space:nowrap}
.info-col h2{font-size:10.3px;font-weight:700;font-style:italic;margin-bottom:11px}
.info-col p{margin-bottom:12px}
.info-col .more{font-style:italic}
.info-col ul{list-style:none;margin-bottom:12px}
.info-col .cont{padding-left:6px}

/* Accreditations */
.affiliations{left:132px;top:643px;width:896px;height:56px;border:1px solid var(--line)}
.affiliations h2{text-align:center;font-size:10.3px;font-weight:600;margin-top:3px}
.affiliation-row{position:absolute;left:44px;top:22px;display:flex;gap:12px;align-items:center}
.badge{height:22px;background:var(--chip)}

/* Footer */
.footer-col{top:715px;font-size:10.3px;line-height:11.8px}
.footer-col h3{font-size:10.3px;font-weight:700}
.footer-col .gap{margin-top:11px}
.footer-right h3{margin-bottom:11.5px}
.social{display:flex;align-items:center;gap:4px;margin-top:6px}
.social-square{width:21px;height:21px;background:var(--navy)}
.social span{font-size:12px;font-weight:600;color:var(--navy)}
</style>
</head>
<body>

<header>
  <div class="abs brand">
    <div class="brand-dot"></div>
    <div class="brand-name">Keystone Drive<br>Services Ltd</div>
  </div>
  <div class="abs header-info">
    <p>Training available across New Zealand</p>
    <p>Head Office - Harbourside, Northvale</p>
    <p>BRANCHES NATIONWIDE</p>
  </div>
  <div class="abs header-pitch">
    <h1>Driver, driving instructor and driver assessor education and training</h1>
    <p>Vehicle types include heavy vehicles, light fleet vehicles, buses, forklifts and specialist machines</p>
    <p>Registered with NQA and NZ Licence Agency Approved Training Provider</p>
    <p class="tagline">Upskilling&nbsp; drivers to be professional, safe and efficient</p>
  </div>
</header>

<nav class="abs main-nav">
  <a style="left:13px">HOME</a>
  <a style="left:68px">ABOUT</a>
  <a style="left:127px">COURSES</a>
  <a style="left:197px">LOCATIONS</a>
  <a style="left:279px">RESOURCES</a>
  <a style="left:360px">LINKS</a>
  <a style="left:414px">FAQs</a>
  <a style="left:465px">ENQUIRY</a>
  <a style="left:534px">CONTACT/MAP</a>
</nav>

<div class="abs gallery-main" role="img" aria-label="Photo of a white and blue driver training tanker truck tilting on a skid pan at a racetrack"></div>
<div class="abs gallery-side" role="img" aria-label="Photo of two driver training tanker trucks parked on an airfield with hills behind"></div>

<div class="abs course-icons">
  <div class="course-icon" title="Licence courses">
    <svg viewBox="0 0 40 40" role="img" aria-label="Licence courses">
      <rect x="4" y="7" width="27" height="27" fill="none" stroke="var(--tick)" stroke-width="3"/>
      <path d="M9 20 L17 28 L35 7" fill="none" stroke="var(--tick)" stroke-width="4"/>
    </svg>
  </div>
  <div class="course-icon" title="Heavy vehicle">
    <svg viewBox="0 0 40 40" role="img" aria-label="Heavy vehicle">
      <rect class="solid" x="2" y="16" width="7" height="9" rx="1"/>
      <rect class="cut" x="3.5" y="17.5" width="4" height="3"/>
      <rect class="solid" x="10" y="14" width="11" height="11"/>
      <rect class="solid" x="23" y="14" width="15" height="11"/>
      <circle class="solid" cx="6" cy="27" r="2.5"/><circle class="solid" cx="17" cy="27" r="2.5"/>
      <circle class="solid" cx="28" cy="27" r="2.5"/><circle class="solid" cx="34" cy="27" r="2.5"/>
    </svg>
  </div>
  <div class="course-icon" title="Light vehicles">
    <svg viewBox="0 0 40 40" role="img" aria-label="Light vehicles">
      <path class="solid" d="M3 27 V15 Q3 12 6 12 H27 Q30 12 32 15 L36 20 Q37 21 37 23 V27 Z"/>
      <path class="cut" d="M25 14 H28 L32 20 H25 Z"/>
      <circle class="solid" cx="10" cy="28" r="3.5"/><circle class="cut" cx="10" cy="28" r="1.5"/>
      <circle class="solid" cx="30" cy="28" r="3.5"/><circle class="cut" cx="30" cy="28" r="1.5"/>
    </svg>
  </div>
  <div class="course-icon" title="Forklifts">
    <svg viewBox="0 0 40 40" role="img" aria-label="Forklifts">
      <rect class="solid" x="8" y="8" width="2.5" height="22"/>
      <path class="stroke" d="M4 30 H10"/>
      <path class="stroke" d="M14 12 H24 L28 20"/>
      <rect class="solid" x="13" y="20" width="22" height="8" rx="1"/>
      <circle class="solid" cx="17" cy="30" r="3"/><circle class="cut" cx="17" cy="30" r="1.2"/>
      <circle class="solid" cx="31" cy="30" r="3"/><circle class="cut" cx="31" cy="30" r="1.2"/>
    </svg>
  </div>
  <div class="course-icon" title="Plant and telehandler">
    <svg viewBox="0 0 40 40" role="img" aria-label="Plant and telehandler">
      <path class="stroke" d="M18 18 L10 7 L4 20"/>
      <path class="solid" d="M2 20 H8 L6 25 Z"/>
      <rect class="solid" x="16" y="14" width="10" height="10" rx="1"/>
      <rect class="cut" x="18" y="16" width="5" height="4"/>
      <rect class="solid" x="14" y="22" width="24" height="5"/>
      <circle class="solid" cx="19" cy="30" r="3.5"/><circle class="cut" cx="19" cy="30" r="1.4"/>
      <circle class="solid" cx="33" cy="30" r="3.5"/><circle class="cut" cx="33" cy="30" r="1.4"/>
    </svg>
  </div>
  <div class="course-icon" title="Elevated work platforms">
    <svg viewBox="0 0 40 40" role="img" aria-label="Elevated work platforms">
      <rect class="solid" x="6" y="9" width="28" height="3"/>
      <path class="stroke" d="M9 13 L31 27 M31 13 L9 27 M9 13 L31 13"/>
      <rect class="solid" x="4" y="27" width="32" height="4"/>
      <circle class="solid" cx="9" cy="33" r="2"/><circle class="solid" cx="31" cy="33" r="2"/>
    </svg>
  </div>
  <div class="course-icon" title="Driving instructors and assessors">
    <svg viewBox="0 0 40 40" role="img" aria-label="Driving instructors and assessors">
      <rect x="6" y="6" width="30" height="20" fill="none" stroke="var(--ink)" stroke-width="2.2"/>
      <path class="stroke" d="M11 12 H28 M11 17 H24 M11 21 H20"/>
      <path class="stroke" d="M16 26 L12 35 M26 26 L30 35"/>
      <path class="stroke" d="M3 33 L14 20"/>
    </svg>
  </div>
  <div class="course-icon" title="Bus, coach and taxi">
    <svg viewBox="0 0 40 40" role="img" aria-label="Bus, coach and taxi">
      <rect class="solid" x="3" y="12" width="34" height="15" rx="3"/>
      <rect class="cut" x="6" y="15" width="5" height="5"/><rect class="cut" x="13" y="15" width="5" height="5"/>
      <rect class="cut" x="20" y="15" width="5" height="5"/><rect class="cut" x="27" y="15" width="7" height="5"/>
      <circle class="solid" cx="10" cy="28" r="3"/><circle class="cut" cx="10" cy="28" r="1.2"/>
      <circle class="solid" cx="30" cy="28" r="3"/><circle class="cut" cx="30" cy="28" r="1.2"/>
    </svg>
  </div>
  <div class="course-icon" title="Four wheel drive and quads">
    <svg viewBox="0 0 40 40" role="img" aria-label="Four wheel drive and quads">
      <path class="solid" d="M4 27 V19 L9 12 H28 L31 18 H36 V27 Z"/>
      <rect class="cut" x="11" y="14" width="7" height="4"/><rect class="cut" x="20" y="14" width="7" height="4"/>
      <rect class="solid" x="1" y="18" width="3" height="7"/>
      <circle class="solid" cx="11" cy="28" r="4"/><circle class="cut" cx="11" cy="28" r="1.6"/>
      <circle class="solid" cx="29" cy="28" r="4"/><circle class="cut" cx="29" cy="28" r="1.6"/>
    </svg>
  </div>
  <div class="course-icon" title="Dangerous goods handling">
    <svg viewBox="0 0 40 40" role="img" aria-label="Dangerous goods handling">
      <rect x="8" y="8" width="24" height="24" fill="var(--hazard)" stroke="var(--ink)" stroke-width="1.5" transform="rotate(45 20 20)"/>
      <rect class="solid" x="7" y="17" width="26" height="6"/>
    </svg>
  </div>
</div>

<section class="abs info-col" style="left:145px">
  <h2>Keystone Drive Services is registered with:</h2>
  <ul>
    <li>- NQA as a PTE (Private Training Establishment)</li>
    <li>- NZ Licence Agency for approved licence courses</li>
    <li>- Skillpath ITO/ SafeWork NZ for forklift training</li>
    <li>- ESA for HSNO Certification</li>
    <li>- Ministry of Roads / NZ Licence Agency for</li>
    <li class="cont">SAFER driver &amp; instructor courses</li>
  </ul>
  <p class="more">Find out more...</p>
</section>

<section class="abs info-col" style="left:442px">
  <h2>Keystone Drive Courses FAQs</h2>
  <p>Find out the answers to the most often asked questions<br>about Keystone Drive courses here...</p>
  <ul>
    <li>- Does Keystone Drive run courses in my location?</li>
    <li>- Do you have advanced driving courses?</li>
    <li>- What accreditation will your (course name) give me?</li>
    <li>- How much does the course I want to do cost?</li>
  </ul>
  <p class="more">Find out more ...</p>
</section>

<section class="abs info-col" style="left:740px">
  <h2>Keystone Drive Courses by Location</h2>
  <ul>
    <li>- Keystone Drive run courses throughout New Zealand.</li>
    <li>- You can find courses by location and enrol online.</li>
    <li>- If you can't find the course you want in your area,</li>
    <li class="cont">please contact us as we can run any course in any</li>
    <li class="cont">location (conditions may apply).</li>
  </ul>
  <p class="more">Browse courses by location...</p>
</section>

<section class="abs affiliations">
  <h2>Accreditations &amp; Affiliations</h2>
  <div class="affiliation-row">
    <div class="badge" style="width:66px"></div>
    <div class="badge" style="width:96px"></div>
    <div class="badge" style="width:44px"></div>
    <div class="badge" style="width:52px"></div>
    <div class="badge" style="width:54px"></div>
    <div class="badge" style="width:48px"></div>
    <div class="badge" style="width:62px"></div>
    <div class="badge" style="width:50px"></div>
    <div class="badge" style="width:40px;height:30px"></div>
    <div class="badge" style="width:88px"></div>
    <div class="badge" style="width:64px"></div>
  </div>
</section>

<footer>
  <div class="abs footer-col" style="left:145px">
    <h3>Home</h3>
    <p>About</p>
    <p>Company accreditations</p>
    <p>Instructors/assessors</p>
    <p>Management admin</p>
    <p>Testimonials</p>
    <p class="gap">Course Locations</p>
    <div class="social"><div class="social-square"></div><span>Find us online</span></div>
  </div>
  <div class="abs footer-col" style="left:360px">
    <h3>Courses</h3>
    <p class="gap">- NZLA Approved Driver Licence &amp; Endorsement Courses</p>
    <p>- Heavy Vehicle</p>
    <p>- Light Vehicle Fleets</p>
    <p>- Forklifts</p>
    <p>- Plant &amp; Telehandler</p>
    <p>- Elevated Work Platforms/Scissor Lifts</p>
    <p>- Driving Instructors &amp; Assessors</p>
    <p>- Bus, Coach &amp; Taxi</p>
    <p>- Four Wheel Drive &amp; Quads</p>
    <p>- HSNO Approved Handler/Filler – Dangerous Goods Handling</p>
  </div>
  <div class="abs footer-col footer-right" style="left:837px">
    <h3>Resources</h3>
    <h3>Links</h3>
    <h3>FAQs/Enquiry</h3>
    <h3>Contact/Map</h3>
    <p style="margin-top:35px">Street map...</p>
  </div>
</footer>

</body>
</html>
```